Stationary Design for Stunning new Logo

I need to envelopes, letterhead, business cards designed to compliment our new logo.

We are a 25 year old printing company going through a brand refresh. All items should have the design extended to both sides for full print ability.

Industry/Entity Type

Printing

Requirements
Must have
• It must utilize the new logo & colors PMS 300 & PMS 295.

```html
<!DOCTYPE html>
<html lang="en">
<head>
<meta charset="utf-8">
<title>Keyline Press – Stationery</title>
<link href="https://fonts.googleapis.com/css2?family=Source+Sans+3:wght@400;600;700;800&display=swap" rel="stylesheet">
<style>
  :root {
    --navy: #0b2a5b;
    --blue: #1f6fc4;
    --ink: #1b1b1b;
    --paper: #ffffff;
    --ground: #f1f1f1;
    --folder-dark: #2b2b2b;
    --folder-light: #7a7a7a;
    --rule: #3d4f8a;
  }
  * { box-sizing: border-box; margin: 0; padding: 0; }
  html, body { width: 1200px; height: 796px; overflow: hidden; }
  body {
    position: relative;
    background: var(--ground);
    font-family: "Source Sans 3", sans-serif;
    color: var(--ink);
  }
  .sheet { position: absolute; background: var(--paper); overflow: hidden; }

  /* brand lockup */
  .lockup { display: flex; align-items: center; gap: 3px; }
  .lockup-dot { border-radius: 50%; background: var(--blue); flex: none; }
  .lockup-name { font-weight: 800; color: var(--navy); letter-spacing: .02em; text-transform: uppercase; white-space: nowrap; }
  .tagline { font-size: 3px; color: var(--blue); letter-spacing: .05em; text-transform: uppercase; white-space: nowrap; }

  /* footer band */
  .band { position: absolute; left: 0; right: 0; display: flex; height: 14px; }
  .band-brand { width: 110px; background: var(--paper); padding-left: 3px; display: flex; flex-direction: column; justify-content: center; }
  .band-navy { flex: 1; background: var(--navy); }
  .band-blue { width: 62px; background: var(--blue); }

  /* letterhead */
  .letterhead { left: 289px; top: 98px; width: 299px; height: 420px; }
  .letterhead-top { position: absolute; top: 16px; left: 0; right: 0; display: flex; justify-content: center; }
  .letterhead-rule { position: absolute; top: 46px; left: 0; right: 0; height: 1px; background: var(--rule); }
  .letter { position: absolute; left: 19px; top: 85px; width: 250px; font-size: 5.2px; line-height: 6.6px; }
  .letter p { margin-bottom: 6.6px; }
  .letter .gap { margin-top: 20px; }
  .letterhead .band { top: 398px; }

  /* folder */
  .folder { left: 632px; top: 82px; width: 350px; height: 449px;
    background: linear-gradient(90deg, var(--folder-dark), var(--folder-light)); }
  .folder-mark { position: absolute; left: 0; right: 0; top: 190px; display: flex; justify-content: center; }
  .folder-mark .lockup-name { color: var(--blue); font-size: 30px; }
  .folder-mark .lockup-dot { width: 26px; height: 26px; margin-right: 8px; }
  .folder .band { top: 413px; }
  .folder .band-brand { background: transparent; }
  .folder .band-navy { background: linear-gradient(90deg, #28364f, var(--navy)); }
  .folder .band-blue { width: 90px; }

  /* business cards */
  .card-back { left: 184px; top: 553px; width: 136px; height: 74px; background: #3a3a3a;
    display: flex; align-items: center; justify-content: center; flex-direction: column; }
  .card-back .lockup-name { color: var(--blue); font-size: 13px; }
  .card-back .lockup-dot { width: 9px; height: 9px; }
  .card-front { left: 184px; top: 645px; width: 136px; height: 77px; }
  .card-details { position: absolute; left: 12px; top: 18px; font-size: 4px; line-height: 5px; color: var(--navy); }
  .card-details .name { font-size: 6px; line-height: 7px; font-weight: 600; }
  .card-details .role { font-weight: 600; margin-bottom: 1px; }
  .card-details span { color: var(--blue); }
  .card-divider { position: absolute; left: 76px; top: 16px; width: 1px; height: 44px; background: #b7c0d2; }
  .card-front .lockup { position: absolute; left: 83px; top: 33px; }
  .card-front .lockup-name { font-size: 7px; }
  .card-front .lockup-dot { width: 5px; height: 5px; }

  /* envelopes */
  .envelope-front { left: 350px; top: 562px; width: 338px; height: 158px;
    background: linear-gradient(180deg, #f7f7f7, #ffffff); }
  .envelope-front .band { top: 142px; }
  .envelope-front .band-blue { width: 68px; }
  .envelope-back { left: 711px; top: 558px; width: 331px; height: 162px; }
  .envelope-flap { position: absolute; left: 0; top: 0; width: 331px; height: 50px; }
  .envelope-back .lockup { position: absolute; left: 0; right: 0; top: 19px; justify-content: center; }
  .envelope-back .lockup-name { font-size: 9px; }
  .envelope-back .lockup-dot { width: 6px; height: 6px; }
  .envelope-back .band { top: 142px; height: 16px; }
  .envelope-back .band-navy { flex: none; width: 225px; }
  .envelope-back .band-blue { flex: 1; }

  .band .lockup-name { font-size: 9px; line-height: 9px; }
  .band .lockup-dot { width: 6px; height: 6px; }
  .folder .band .lockup-name { color: var(--blue); }

  /* pencil */
  .pencil { position: absolute; left: 229px; top: 275px; }
</style>
</head>
<body>

  <svg class="pencil" width="12" height="240" viewBox="0 0 12 240" aria-hidden="true">
    <path d="M6 0 L9 18 L3 18 Z" fill="#c9b69a"/>
    <path d="M6 0 L7 6 L5 6 Z" fill="#2c2c2c"/>
    <rect x="3" y="18" width="6" height="220" rx="1" fill="#2f4a45"/>
  </svg>

  <section class="sheet letterhead">
    <div class="letterhead-top">
      <div class="lockup"><span class="lockup-dot" style="width:6px;height:6px"></span><span class="lockup-name" style="font-size:9px">Keyline Press</span></div>
    </div>
    <div class="letterhead-rule"></div>
    <div class="letter">
      <p>220 Harbor View Road<br>Portland, OR 97201.</p>
      <p>January 29th, 2011</p>
      <p>Mr. Aldine<br>President, Aldine Learning House<br>58 Maple Court<br>Boston, MA 02108</p>
      <p>Dear Mr. Aldine:</p>
      <p>In the first paragraph, one needs to give a brief introduction of oneself. One should also give reference to the purpose of the letter in brief.<br>The second paragraph needs to give the details of the letter and its need. This paragraph is mostly longer than the others and plays the main role in the letter. Keep the sentences short and to the point. Avoid using complex words and sentences.</p>
      <p class="gap">The third and last paragraph is the conclusion of the letter and can be kept short.</p>
      <p>Sincerely,</p>
      <p>(this is where the signature of the writer will be placed)</p>
      <p>Dana Whitlow<br>Read more at Letterwise: http://www.letterwise.example/guides/letter-layout.html</p>
    </div>
    <div class="band">
      <div class="band-brand">
        <div class="lockup"><span class="lockup-dot"></span><span class="lockup-name">Keyline Press</span></div>
        <div class="tagline">Sharp service • true colour • fair pricing</div>
      </div>
      <div class="band-navy"></div><div class="band-blue"></div>
    </div>
  </section>

  <section class="sheet folder">
    <div class="folder-mark">
      <div class="lockup"><span class="lockup-dot"></span><span class="lockup-name">Keyline Press</span></div>
    </div>
    <div class="band">
      <div class="band-brand">
        <div class="lockup"><span class="lockup-dot"></span><span class="lockup-name">Keyline Press</span></div>
        <div class="tagline">Sharp service • true colour • fair pricing</div>
      </div>
      <div class="band-navy"></div><div class="band-blue"></div>
    </div>
  </section>

  <section class="sheet card-back">
    <div class="lockup"><span class="lockup-dot"></span><span class="lockup-name">Keyline Press</span></div>
    <div class="tagline" style="font-size:3.5px">Sharp service • true colour • fair pricing</div>
  </section>

  <section class="sheet card-front">
    <div class="card-details">
      <div class="name">Your Name</div>
      <div class="role">Position</div>
      <div>Address: <span>000 Street Name, City</span></div>
      <div><span>State 00000</span></div>
      <div>Phone: <span>000 000 0000</span></div>
      <div style="margin-top:3px">Fax: <span>000 000 0000</span></div>
      <div>Email: <span>name@mail.com</span></div>
    </div>
    <div class="card-divider"></div>
    <div class="lockup"><span class="lockup-dot"></span><span class="lockup-name">Keyline</span></div>
  </section>

  <section class="sheet envelope-front">
    <div class="band">
      <div class="band-brand">
        <div class="lockup"><span class="lockup-dot"></span><span class="lockup-name">Keyline Press</span></div>
        <div class="tagline">Sharp service • true colour • fair pricing</div>
      </div>
      <div class="band-navy"></div><div class="band-blue"></div>
    </div>
  </section>

  <section class="sheet envelope-back">
    <svg class="envelope-flap" viewBox="0 0 331 50" aria-hidden="true">
      <path d="M0 0 H331 L318 46 H13 Z" fill="#ffffff" stroke="#d8d8d8" stroke-width="1"/>
    </svg>
    <div class="lockup"><span class="lockup-dot"></span><span class="lockup-name">Keyline Press</span></div>
    <div class="band"><div class="band-navy"></div><div class="band-blue"></div></div>
  </section>

</body>
</html>
```